Stationery Design Project

We need a stationery design for our Norwegian trucking company. We have existed for about 15 years and our 12 drivers uses relatively new vehicles to transport goods around in northern Norway. Long distance routes with fresh fish og food transport is our main operations.

We have already made alogo that's printed on our trucks. The logo and a picture of our trucks is attached. I think the logo i crappy, but since its already in use, changing it is not an option in this round. Still using a better colour scheme in the overall stationery and more interesting fonts is possible (altso in the logo).

Company details:
Name: Vikstrandbil AS
Organisation nr 981 537 608
Post adress: 8613 Lysvær

I like minimalism and simplicity. I am avalibly for questions in normal GMT working hours either here or on mail: petter@vikstrand.no

Reason: Hi. Im extending the deadline because I needed some time to find a vector file of our logo. Sorry for the inconvenience

Hi, and thanks for all your interest in the project. Some updates:

-          I have decided to commit to using one of the designs. Some designer will get the payment.

-          I have extended the deadline with 24 hours since I needed some time to find our firms vector logo (a slow Swedish man was holding me up)

-          We will not choose a design before the deadline. No need to rush.

-          We have received a lot of great design and think there is a need to specified the product we want to make:

o   Business Card for all our employers. I just need the design and will duplicate with the correct numbers and name myself. The information on should be: Logo, employer’s name, Phone number, email, website, Postal number and address. Use this as a template: logo, Leif Brattli, 47283916, Leif@vikstrand.no,, vikstrand.no, 8613 Lysvær. The order and placement of the information is your creative decision.

o   Stickers to put on the goods we travel. On the sticker the should be the following information: Logo, phone number, Tekst and link: Fraktæ av Vikstrandbil. Ke du syns? Vikstrand.no/tilbakemelding (this means: Handled by Vikstrandbil. What do you think Vikstrand.no/feedback -à the link will be a feedback form). The placement the information and size is your creative decision with some stings: we have been thinking of using Prentavo for printing and see that a size about 6x6 cm, 8x5 or something like that. (with 3000 copies our budget is 200 punds). Any suggestions of other suppliers are welcome. Prentavo price calculator http://www.prentavoprint.co.uk/digital-litho-printing/printing-labels-tags/stickers/

o   Letterhead with logo, address, phone number and organizational number.

o   Envelopes with logo,address, phone number and organizational number.

Have a nice day.

 

 

• Using the blue colour in the logo and using a similar graphic approch.

```html
<!DOCTYPE html>
<html lang="no">
<head>
<meta charset="utf-8">
<title>Vikstrandbil Business Card</title>
<link rel="stylesheet" href="https://fonts.googleapis.com/css2?family=Source+Sans+3:wght@400;600&display=swap">
<style>
  :root {
    --page: #e9eaec;
    --card-white: #ffffff;
    --navy: #1d2a7a;
    --brand-blue: #1d72b8;
    --text-grey: #7a7a7a;
    --rule-grey: #b5b5b5;
    --back-deep: #232c8e;
    --back-light: #2580b0;
  }
  * { margin: 0; padding: 0; box-sizing: border-box; }
  html, body { width: 1200px; height: 900px; overflow: hidden; }
  body {
    background: var(--page);
    font-family: "Source Sans 3", Arial, sans-serif;
    position: relative;
  }
  .card {
    position: absolute;
    width: 620px;
    height: 354px;
    box-shadow: 0 6px 18px rgba(0,0,0,0.18);
  }
  .card-back {
    left: 530px;
    top: 56px;
    background: radial-gradient(ellipse at 45% 85%, var(--back-light) 0%, #2459a6 45%, var(--back-deep) 100%);
    display: flex;
    align-items: center;
    justify-content: center;
  }
  .card-back .wordmark {
    color: #ffffff;
    font-size: 52px;
    font-weight: 600;
    letter-spacing: 0.5px;
  }
  .card-front {
    left: 50px;
    top: 480px;
    background: var(--card-white);
  }
  .front-logo {
    position: absolute;
    left: 36px;
    top: 36px;
    display: flex;
    align-items: center;
    gap: 12px;
  }
  .front-logo .mark-dot {
    width: 22px;
    height: 22px;
    border-radius: 50%;
    background: var(--brand-blue);
  }
  .front-logo .wordmark {
    color: var(--navy);
    font-size: 38px;
    font-weight: 600;
  }
  .divider {
    position: absolute;
    left: 36px;
    right: 36px;
    top: 178px;
    height: 1px;
    background: linear-gradient(to right, rgba(181,181,181,0), var(--rule-grey) 70%, var(--rule-grey));
  }
  .contact-list {
    position: absolute;
    left: 36px;
    top: 196px;
    list-style: none;
    color: var(--text-grey);
    font-size: 17px;
    line-height: 24px;
  }
  .contact-list li { display: flex; align-items: center; gap: 12px; }
  .contact-list svg { width: 14px; height: 14px; fill: var(--brand-blue); flex: none; }
  .person {
    position: absolute;
    right: 36px;
    top: 190px;
    text-align: right;
  }
  .person .name {
    color: var(--brand-blue);
    font-size: 26px;
    font-weight: 600;
    line-height: 30px;
    padding-bottom: 3px;
    border-bottom: 1.5px solid var(--text-grey);
  }
  .person .role {
    color: var(--text-grey);
    font-size: 17px;
    line-height: 24px;
  }
  .address {
    position: absolute;
    right: 36px;
    bottom: 28px;
    text-align: right;
    color: var(--text-grey);
    font-size: 17px;
    line-height: 23px;
    font-style: normal;
  }
</style>
</head>
<body>

  <section class="card card-back" aria-label="Business card back">
    <span class="wordmark">Vikstrandbil</span>
  </section>

  <section class="card card-front" aria-label="Business card front">
    <div class="front-logo">
      <span class="mark-dot"></span>
      <span class="wordmark">Vikstrandbil</span>
    </div>

    <div class="divider"></div>

    <ul class="contact-list">
      <li>
        <svg viewBox="0 0 16 16" aria-hidden="true"><path d="M1 5c0-2 3-3 7-3s7 1 7 3v1h-4V4.5H5V6H1zM4 8h8l2 6H2z"/></svg>
        75 77 21 40
      </li>
      <li>
        <svg viewBox="0 0 16 16" aria-hidden="true"><rect x="1" y="11" width="2.5" height="4"/><rect x="5" y="8" width="2.5" height="7"/><rect x="9" y="5" width="2.5" height="10"/><rect x="13" y="2" width="2.5" height="13"/></svg>
        47283916
      </li>
      <li>
        <svg viewBox="0 0 16 16" aria-hidden="true"><path d="M1 3h14v10H1zM2 4.2v.6l6 4 6-4v-.6zM2 6.3V12h12V6.3l-6 4z" fill-rule="evenodd"/></svg>
        Leif@vikstrand.no
      </li>
      <li>
        <svg viewBox="0 0 16 16" aria-hidden="true"><circle cx="8" cy="8" r="7"/><path d="M1 8h14M8 1c-3 3-3 11 0 14M8 1c3 3 3 11 0 14" stroke="#fff" stroke-width="1" fill="none"/></svg>
        www.vikstrand.no
      </li>
    </ul>

    <div class="person">
      <p class="name">Leif Brattli</p>
      <p class="role">Marketing Manager</p>
    </div>

    <address class="address">
      Vikstrandveien 12<br>
      8613 Lysvær
    </address>
  </section>

</body>
</html>
```